Design for Marketing Consulting Agency - Please see attachments

Looking for a very simple site - 3-5 pages, one with a portfolio page to showcase our work where we can leave comments on it. Looking for modern/clean/impactful design to represent our brand. Here is example of what I like: https://www.norvika.example/en-us/ logo and mood board and copy for website (minus the portfolio). Prefer black/gray/white with pops of color/imagery that come from the logo. Prefer dark hero, more white and pops of the orange and red for the rest of the site.

Target Market(s)

Small to medium size businesses

Font styles to use
Sans Serif

Colors

Designer to choose only greyscale colors for use in the design.

Requirements
Must have
• Please see mood board. Prefer mostly black/white site with pops of color and imagery.
Nice to have
• Sample portfolio page?
Should not have
• Don't make it look 'futuristic' . Try to make it modern and clean.

```html
<!DOCTYPE html>
<html lang="en">
<head>
<meta charset="utf-8">
<title>Bright Signal Marketing</title>
<link rel="stylesheet" href="https://fonts.googleapis.com/css2?family=Comfortaa:wght@300;700&family=Righteous&family=Montserrat:wght@400;500;600;700&display=swap">
<style>
:root{
  --gold:#c8911b;
  --red:#e6412b;
  --ink:#2f2f2f;
  --dark:#333333;
  --slate:#5e6a6b;
  --slate-deep:#505b5c;
  --white:#ffffff;
  --text:#3a3a3a;
}
*{box-sizing:border-box;margin:0;padding:0}
html,body{width:1200px;height:4543px;overflow:hidden}
body{position:relative;font-family:"Montserrat",sans-serif;color:var(--text);background:var(--white)}
.abs{position:absolute}
.light{font-family:"Comfortaa",sans-serif;font-weight:300}
.bold{font-family:"Righteous",sans-serif;font-weight:400}
.btn{position:absolute;display:flex;align-items:center;justify-content:center;gap:8px;background:var(--red);color:var(--white);font-family:"Comfortaa",sans-serif;font-weight:700;font-size:16px;border-radius:3px;white-space:nowrap}
.btn::after{content:"";width:14px;height:14px;border-radius:50%;background:var(--white)}
.brand{position:absolute;display:flex;align-items:center;gap:14px;color:var(--white)}
.brand-mark{width:22px;height:22px;background:var(--gold)}
.brand-name{font-family:"Montserrat",sans-serif;font-weight:500;font-size:23px;line-height:25px;letter-spacing:.5px}

/* hero */
.hero{position:absolute;left:0;top:0;width:1200px;height:662px;border-bottom-left-radius:150px;overflow:hidden;background:radial-gradient(ellipse at 55% 25%,#3c4c78 0%,#1d2647 45%,#151a2c 70%),#151a2c}
.hero-rock{position:absolute;left:0;bottom:0;width:1200px;height:300px;background:linear-gradient(180deg,rgba(70,55,50,0) 0%,#3a2c28 55%,#241b19 100%)}
.nav{position:absolute;color:var(--white);font-family:"Comfortaa",sans-serif;font-weight:700;font-size:15px}
.nav a{position:absolute;white-space:nowrap;color:var(--white);text-decoration:none}
.hero-title{position:absolute;left:0;width:1200px;text-align:center;color:var(--white);font-size:52px;line-height:66px}
.hero-sub{position:absolute;left:180px;width:840px;text-align:center;color:var(--white);font-size:20px;line-height:37px}
.circle-arrow{position:absolute;width:38px;height:38px}

.h-xl{font-size:54px;line-height:64px;color:var(--ink)}
.para{font-size:16px;line-height:27.5px}

/* cards */
.card{position:absolute;top:1994px;width:309px;height:415px;background:var(--white);border-radius:18px;box-shadow:0 4px 14px rgba(0,0,0,.12);text-align:center}
.card.featured{background:var(--slate);color:var(--white)}
.card h3{font-family:"Comfortaa",sans-serif;font-weight:700;font-size:21px;line-height:29px;margin-top:28px;color:var(--ink)}
.card.featured h3{color:var(--white)}
.price{font-family:"Montserrat",sans-serif;font-weight:700;font-size:31px;margin-top:8px;color:var(--ink)}
.card.featured .price{color:var(--white)}
.card ul{list-style:none;text-align:left;padding:0 16px 0 20px;margin-top:12px}
.card li{position:relative;padding-left:22px;font-size:16px;line-height:24px;margin-bottom:9px}
.card li::before{content:"";position:absolute;left:2px;top:6px;width:12px;height:12px;background:var(--gold)}
.card .btn{left:33px;top:336px;width:243px;height:49px;font-size:15px}

/* team */
.member{position:absolute;width:200px;text-align:center;color:var(--white)}
.member .ring{width:194px;height:194px;margin:0 auto;border-radius:50%;border:3px solid var(--gold);padding:8px}
.member .photo{width:100%;height:100%;border-radius:50%;background:linear-gradient(180deg,#ffffff 0%,#e9ecec 60%,#c9cfd0 100%)}
.member .name{font-family:"Righteous",sans-serif;font-size:17px;margin-top:14px;line-height:20px}
.member .role{font-size:15px;line-height:20px}

.tile{position:absolute;width:304px;height:195px;box-shadow:0 3px 10px rgba(0,0,0,.15);border:5px solid var(--white)}

.field{position:absolute;border:1px solid #8a8a8a;background:var(--dark);color:#d6d6d6;font-size:15px;padding:10px 12px}

.foot-h{position:absolute;font-family:"Righteous",sans-serif;font-size:18px;color:var(--white)}
.foot-h::after{content:"";position:absolute;left:0;top:32px;width:38px;height:3px;background:var(--gold)}
.foot-link{position:absolute;font-size:15px;color:var(--white)}
.foot-link::before{content:"›";color:var(--red);margin-right:8px}
.foot-text{position:absolute;font-size:14px;line-height:26px;color:var(--white);white-space:nowrap}
.social{position:absolute;top:4373px;width:36px;height:36px;border-radius:50%;background:var(--white)}
</style>
</head>
<body>

<section class="hero">
  <div class="abs" role="img" aria-label="Night sky full of stars above a rocky summit with a lone hiker standing on top" style="inset:0"></div>
  <div class="hero-rock" role="img" aria-label="Rocky mountain silhouette"></div>

  <div class="brand" style="left:99px;top:26px">
    <span class="brand-mark"></span>
    <span class="brand-name">BRIGHT<br>SIGNAL<br>MARKETING</span>
  </div>

  <nav class="nav" style="left:0;top:52px">
    <a style="left:466px">Our Packages</a>
    <a style="left:627px">Our Work</a>
    <a style="left:750px">Our Team</a>
    <a style="left:872px">Contact</a>
  </nav>
  <div class="btn" style="left:971px;top:42px;width:132px;height:41px">Portfolio</div>

  <svg class="circle-arrow" style="left:99px;top:325px" viewBox="0 0 38 38"><circle cx="19" cy="19" r="18" fill="#fff"/><path d="M22 11 L14 19 L22 27" fill="none" stroke="#1d2647" stroke-width="4"/></svg>
  <svg class="circle-arrow" style="left:1062px;top:325px" viewBox="0 0 38 38"><circle cx="19" cy="19" r="18" fill="#fff"/><path d="M16 11 L24 19 L16 27" fill="none" stroke="#1d2647" stroke-width="4"/></svg>

  <h1 class="hero-title" style="top:308px"><span class="bold">We Deliver</span> <span class="light">Simple, Clear, and</span><br><span class="light">Impactful</span> <span class="bold">Messaging and Designs</span></h1>
  <p class="hero-sub" style="top:448px">It's an unfortunate fact – many business owners overthink their marketing. They try to be overly creative or wordy.</p>
  <div class="btn" style="left:512px;top:542px;width:175px;height:44px">Discover More</div>
  <svg class="abs" style="left:592px;top:603px" width="26" height="44" viewBox="0 0 26 44"><rect x="2" y="2" width="22" height="40" rx="11" fill="none" stroke="#fff" stroke-width="3"/><rect x="11.5" y="9" width="3" height="9" rx="1.5" fill="#fff"/></svg>
</section>

<section>
  <h2 class="abs h-xl" style="left:97px;top:738px"><span class="light">Welcome to</span><br><span class="bold">Bright Signal<br>Marketing</span></h2>
  <p class="abs para" style="left:99px;top:948px;width:490px">It's an unfortunate fact – many business owners overthink their marketing. They try to be overly creative or wordy, resulting in empty statements, confused consumers, and lost revenue opportunities. Bright Signal Marketing has a simple, thorough process that we use to understand your customer base and their unique pain points</p>
  <div class="btn" style="left:99px;top:1142px;width:173px;height:46px">Read More</div>

  <svg class="abs" style="left:679px;top:714px" width="521" height="548" viewBox="0 0 521 548"><circle cx="274" cy="274" r="274" fill="var(--gold)"/><circle cx="274" cy="274" r="222" fill="#f4f1ec"/></svg>
  <div class="abs" role="img" aria-label="Young woman working on a laptop while sitting on a grey bean bag" style="left:600px;top:770px;width:480px;height:450px;border-radius:50% 50% 30% 30%;background:linear-gradient(180deg,#efe6dc 0%,#b9b2aa 60%,#8f8b88 100%)"></div>
</section>

<section class="abs" style="left:0;top:1327px;width:1200px;height:517px;background:var(--dark);border-top-right-radius:140px">
  <div class="abs" role="img" aria-label="Smiling man in a denim shirt holding an open laptop" style="left:106px;top:32px;width:476px;height:459px;background:linear-gradient(180deg,#4a4a4a 0%,#8aa2b8 45%,#6f8aa3 100%);border-radius:80px 0 0 80px"></div>
  <h2 class="abs" style="left:611px;top:113px;font-size:52px;line-height:60px;color:var(--white)"><span class="light">Who</span> <span class="bold">Are We?</span></h2>
  <p class="abs para" style="left:614px;top:187px;width:500px;color:var(--white)">Bright Signal Marketing is a Marketing Agency that delivers a breadth of services from brand/rebrand, strategy, design, and web to digital and print marketing campaigns and trade shows. We bring over 20 years of experience in marketing for both B2B to B2C organizations ranging from 5M to over 200M.</p>
  <div class="btn" style="left:614px;top:378px;width:173px;height:45px">Read More</div>
</section>

<section>
  <h2 class="abs" style="left:0;width:1200px;top:1904px;text-align:center;font-size:54px;line-height:64px;color:var(--ink)"><span class="light">Our</span> <span class="bold">Packages</span></h2>

  <div class="card" style="left:99px">
    <h3>Website &amp; Messaging<br>Facelift</h3>
    <div class="price">$3000-$4000</div>
    <ul style="margin-top:20px">
      <li>Two homepage mockups.</li>
      <li>One mood board.</li>
      <li>Two versions of value proposition messaging – x words</li>
    </ul>
    <div class="btn">See Case Study</div>
  </div>

  <div class="card featured" style="left:445px">
    <h3>Simple Brand Rebuild</h3>
    <div class="price">$5000-$6000</div>
    <p style="font-size:16px;margin-top:6px">Meetings necessary: <strong style="font-weight:500">6-7 hours</strong></p>
    <ul style="margin-top:18px">
      <li>5 logo concepts</li>
      <li>Two homepage mockups</li>
      <li>One brand storyboard Two versions of value proposition messaging</li>
    </ul>
    <div class="btn">See example case study</div>
  </div>

  <div class="card" style="left:791px">
    <h3>Additional Services<br>Offered</h3>
    <ul style="margin-top:10px">
      <li>Strategic Consulting on Growth Strategies and Building Teams</li>
      <li>Trade Show Management and Booth Designs</li>
      <li>Email Marketing Campaigns</li>
      <li>Digital Marketing Campaigns</li>
    </ul>
    <div class="btn">See Case Study</div>
  </div>
</section>

<section class="abs" style="left:0;top:2471px;width:1200px;height:639px;background:var(--slate)">
  <svg class="abs" style="left:0;top:0" width="640" height="622" viewBox="0 0 640 622"><path d="M0 140 Q0 0 150 0 L330 0 A310 310 0 0 1 330 620 L0 620 Z" fill="var(--slate-deep)"/></svg>
  <h2 class="abs" style="left:97px;top:130px;font-size:54px;line-height:64px;color:var(--white)"><span class="light">Meet</span> <span class="bold">The Team</span></h2>
  <p class="abs para" style="left:99px;top:202px;width:410px;color:var(--white)">Bright Signal Marketing is run and managed by Marlene Okafor. It has a team of experts from content creation to graphic design and digital marketing. Marlene is a passionate marketing visionary with 20+ years of experience leading direct and channel marketing teams and creating powerful and effective multi-channel marketing strategies and campaigns.</p>
  <div class="btn" style="left:101px;top:447px;width:173px;height:45px">Read More</div>

  <div class="member" style="left:640px;top:69px"><div class="ring"><div class="photo" role="img" aria-label="Portrait of a male designer in a grey suit"></div></div><div class="name">Daniel Harrow</div><div class="role">Designer</div></div>
  <div class="member" style="left:901px;top:69px"><div class="ring"><div class="photo" role="img" aria-label="Portrait of a female designer in a white blazer"></div></div><div class="name">Sofia Varenne</div><div class="role">Designer</div></div>
  <div class="member" style="left:640px;top:348px"><div class="ring"><div class="photo" role="img" aria-label="Portrait of a female designer in a dark suit"></div></div><div class="name">Nora Lindqvist</div><div class="role">Designer</div></div>
  <div class="member" style="left:901px;top:348px"><div class="ring"><div class="photo" role="img" aria-label="Portrait of a male designer in a navy t-shirt"></div></div><div class="name">Peter Calloway</div><div class="role">Designer</div></div>
</section>

<section>
  <h2 class="abs bold" style="left:0;width:1200px;top:3168px;text-align:center;font-size:54px;line-height:64px;color:var(--ink)">Portfolio</h2>
  <div class="tile" role="img" aria-label="Agency website homepage mockup" style="left:102px;top:3248px;background:linear-gradient(135deg,#1c2340 0%,#2c2a4f 60%,#e7e7ee 60%)"></div>
  <div class="tile" role="img" aria-label="Stationery and business card set mockup" style="left:448px;top:3248px;background:linear-gradient(135deg,#6d7171 0%,#3e4242 100%)"></div>
  <div class="tile" role="img" aria-label="Logo design sample on red background" style="left:794px;top:3248px;background:linear-gradient(135deg,#ee4a2d 0%,#d93a22 100%)"></div>
  <div class="tile" role="img" aria-label="White t-shirt mockup on sage background" style="left:102px;top:3474px;background:linear-gradient(135deg,#8aa596 0%,#6e8c7c 100%)"></div>
  <div class="tile" role="img" aria-label="Coffee packaging design mockup" style="left:448px;top:3474px;background:linear-gradient(135deg,#c8b89a 0%,#9e8a69 100%)"></div>
  <div class="tile" role="img" aria-label="Business card design on dark surface" style="left:794px;top:3474px;background:linear-gradient(135deg,#2b2b2b 0%,#555 100%)"></div>
</section>

<section class="abs" style="left:0;top:3742px;width:1200px;height:423px;background:var(--dark);border-top-right-radius:140px">
  <h2 class="abs" style="left:536px;top:74px;font-size:54px;line-height:64px;color:var(--white)"><span class="light">Get</span> <span class="bold">In Touch</span></h2>
  <div class="field" style="left:538px;top:146px;width:276px;height:42px">Name</div>
  <div class="field" style="left:538px;top:198px;width:276px;height:40px">Email</div>
  <div class="field" style="left:538px;top:248px;width:276px;height:41px">Phone</div>
  <div class="field" style="left:824px;top:146px;width:276px;height:143px">Message</div>
  <div class="btn" style="left:540px;top:303px;width:147px;height:43px">Submit</div>
</section>
<div class="abs" role="img" aria-label="Smiling woman holding an open laptop" style="left:0;top:3716px;width:460px;height:449px;background:linear-gradient(180deg,#e9d9b8 0%,#b9b4ad 50%,#8c8784 100%);border-radius:0 200px 0 0"></div>

<footer class="abs" style="left:0;top:4165px;width:1200px;height:378px;background:var(--slate)">
  <div class="brand" style="left:99px;top:106px">
    <span class="brand-mark"></span>
    <span class="brand-name">BRIGHT<br>SIGNAL<br>MARKETING</span>
  </div>
</footer>
<span class="social" style="left:98px"></span>
<span class="social" style="left:148px"></span>
<span class="social" style="left:197px"></span>

<div class="foot-h" style="left:385px;top:4224px">Quick Links</div>
<div class="foot-link" style="left:385px;top:4282px">Our Packages</div>
<div class="foot-link" style="left:385px;top:4326px">Our Work</div>
<div class="foot-link" style="left:385px;top:4377px">Our Team</div>
<div class="foot-link" style="left:385px;top:4430px">Contact</div>

<div class="foot-h" style="left:567px;top:4224px">Contact Us</div>
<svg class="abs" style="left:567px;top:4283px" width="14" height="18" viewBox="0 0 14 18"><path d="M7 0 A7 7 0 0 1 14 7 C14 12 7 18 7 18 C7 18 0 12 0 7 A7 7 0 0 1 7 0 Z" fill="var(--red)"/><circle cx="7" cy="7" r="2.5" fill="var(--slate)"/></svg>
<div class="foot-text" style="left:588px;top:4279px">12 Harbour Lane, Suite 200<br>Sydney, Australia</div>
<svg class="abs" style="left:566px;top:4347px" width="16" height="12" viewBox="0 0 16 12"><rect width="16" height="12" rx="1" fill="var(--red)"/><path d="M0 1 L8 7 L16 1" fill="none" stroke="var(--slate)" stroke-width="1.5"/></svg>
<div class="foot-text" style="left:588px;top:4340px">info@brightsignal.example</div>
<svg class="abs" style="left:566px;top:4382px" width="16" height="16" viewBox="0 0 16 16"><path d="M3 1 L6 1 L7 5 L5 6.5 C6 9 7 10 9.5 11 L11 9 L15 10 L15 13 C15 14 14 15 13 15 C6 15 1 10 1 3 C1 2 2 1 3 1 Z" fill="var(--red)"/></svg>
<div class="foot-text" style="left:588px;top:4377px">01 555 010 789</div>

<div class="foot-h" style="left:844px;top:4224px">Newsletter</div>
<div class="abs" style="left:844px;top:4287px;width:257px;height:39px;background:#eef1f1;border-radius:2px;font-size:14px;color:#8b9494;padding:10px 18px">Enter email address</div>
<div class="btn" style="left:844px;top:4339px;width:257px;height:40px">Subscribe</div>

<div class="abs" style="left:99px;top:4488px;width:1002px;height:1px;background:#8a9596"></div>
<div class="abs" style="left:0;width:1200px;top:4504px;text-align:center;font-size:14px;color:#e4e8e8">© 2022 <span style="color:var(--gold)">Bright Signal Marketing.</span> All right reserved</div>

</body>
</html>
```